Education / Investment Website Design (PDF Wireframe Provided)

More details are in the wireframe document

We need a website design for an investment education company. Our Clients purchase education courses through us. We use meridian toolkit (Wordpress) for our website. We just require the graphics in PSD (not coded) for the

1. Homepage - brightfunnelhub.com style
2. Blog page - brightfunnelhub.com style
3. Single Blog Post
4. Product page - Lernova.com style
5. Single Product Page - https://www.lernova.com/share-market-class-oceania/?ref=kP7qLmW3xT9Z
6. Contact Us Page (Contact Us Form, Map and Contact details)
7. About Us Page

See the attached Wireframe for the homepage

IMPORTANT
Websites we like are clean, white, similar to BrightFunnelHub.com and Lernova.com
Use of white space, big fonts, flat buttons

Attached wireframe is the flow of the homepage. (Homepage brief PDF)

Each section represents a "fold" as visitors are scrolling down. (Homepage showing folds PDF - how the visitor sees each section of the homepage as they scroll down the homepage)

We've got a clear idea of the elements on the page and looking for a great graphic / web designer to create those for us. (We do the coding)

Website currently is: southerncrosswealthschool.com.au (we want to simplify the website and have a more modern / flat design)

Questions: Please ask

Target Market(s)

Investors, People looking for Investment / Financial Education

Industry/Entity Type

Investment

Number of Pages Required

5+ page

Font styles to use
Sans Serif

Requirements
Must have
• Similar Items listed in the wireframe
• Clean Look - Flat design - elegant
• Roll-over (mouse on / mouse off) for Buttons and Top Banner Selection
Should not have
• Images that looks too much like "Stock Images"
• Please avoid bright orange

```html
<!DOCTYPE html>
<html lang="en">
<head>
<meta charset="utf-8">
<title>Blog – Southern Cross Wealth School</title>
<link rel="stylesheet" href="https://fonts.googleapis.com/css2?family=Lato:wght@300;400;700&family=Montserrat:wght@400;600;700&display=swap">
<style>
:root{
  --teal:#6bc9c5;
  --teal-dark:#14928e;
  --teal-icon:#4fb3af;
  --topbar:#4d4d4d;
  --search:#6e6e6e;
  --ink:#222;
  --text:#555;
  --muted:#888;
  --side-grey:#cfcfcf;
  --tab-grey:#c4c4c4;
  --footer:#686868;
  --share-a:#3b5a9a;
  --share-b:#2aa3d9;
  --share-c:#d6503c;
  --share-off:#cccccc;
  --white:#fff;
}
*{box-sizing:border-box;margin:0;padding:0}
html,body{width:1200px;height:3315px;overflow:hidden;background:var(--white)}
body{position:relative;font-family:'Lato',sans-serif;color:var(--text)}
a{color:inherit;text-decoration:none}

.topbar{position:absolute;left:0;top:0;width:1200px;height:38px;background:var(--topbar)}
.topbar__note{position:absolute;left:160px;top:0;line-height:38px;font:600 12.5px 'Montserrat',sans-serif;color:var(--white)}
.topbar__search{position:absolute;left:844px;top:0;width:206px;height:38px;background:var(--search);color:#eee;font-size:13px;line-height:38px;padding-left:16px}
.topbar__search svg{position:absolute;right:16px;top:12px}

.header{position:absolute;left:0;top:38px;width:1200px;height:90px;background:var(--teal)}
.brand{position:absolute;left:137px;top:22px;display:flex;align-items:center;gap:10px;color:var(--white)}
.brand__dot{width:42px;height:42px;border-radius:50%;background:#2f6f8c}
.brand__name{font:700 27px 'Lato',sans-serif;letter-spacing:1px}
.header__account{position:absolute;right:150px;top:10px;font:600 12px 'Montserrat',sans-serif;color:var(--white);display:flex;gap:22px}
.nav{position:absolute;right:150px;top:58px;display:flex;gap:28px;font:600 12.5px 'Montserrat',sans-serif;color:var(--white)}
.nav .is-active{color:#1d5e5c}

.hero{position:absolute;left:0;top:128px;width:1200px;height:122px;background:linear-gradient(90deg,#5fb9b5 0%,#7fd0cc 45%,#68c4c0 100%)}
.hero__title{position:absolute;left:0;top:0;width:100%;line-height:122px;text-align:center;font:400 42px 'Lato',sans-serif;color:var(--white);letter-spacing:1px}

.side-tabs{position:absolute;left:1152px;top:181px;display:flex;flex-direction:column;gap:8px}
.side-tabs span{display:block;width:48px;height:40px;background:var(--tab-grey)}

.crumbs{position:absolute;left:137px;top:265px;font-size:13px;color:#666}
.crumbs b{color:#333}

.post{position:absolute;left:137px;width:524px;height:667px}
.post__title{font:400 42px/52px 'Lato',sans-serif;color:var(--ink)}
.post__meta{position:absolute;top:64px;left:0;display:flex;gap:26px;font-size:12.5px;color:#333;align-items:center}
.post__meta span{display:flex;align-items:center;gap:6px}
.post__image{position:absolute;top:122px;left:0;width:524px;height:232px;background:linear-gradient(100deg,#b9c7d4 0%,#e8d9b0 45%,#f3e2b8 60%,#cdb98d 100%)}
.post__excerpt{position:absolute;top:397px;left:0;font-size:16.5px;line-height:27px;color:#444}
.share{position:absolute;top:491px;left:0;display:flex;gap:9px}
.share__btn{width:97px;height:25px;display:flex;align-items:center;justify-content:space-between;padding:0 14px;color:var(--white);font-size:12px}
.share__btn i{display:block;width:10px;height:10px;border-radius:50%;background:var(--white)}
.share__btn--a{background:var(--share-a)}
.share__btn--b{background:var(--share-b)}
.share__btn--c{background:var(--share-c)}
.share__btn--off{background:var(--share-off)}
.share__btn--comments{background:var(--teal)}
.btn-more{position:absolute;top:564px;left:0;width:115px;height:48px;background:var(--teal-dark);color:var(--white);font:700 13px/48px 'Lato',sans-serif;text-align:center}

.cta{position:absolute;left:767px;width:283px;height:48px;background:var(--teal);color:var(--white);display:flex;align-items:center;font:700 12.5px 'Lato',sans-serif}
.cta__icon{width:48px;height:48px;display:flex;align-items:center;justify-content:center}
.cta__label{flex:1;text-align:center;padding-right:10px}

.popular{position:absolute;left:767px;top:599px;width:283px;height:192px;background:var(--side-grey)}
.popular__title{text-align:center;font:400 26px 'Lato',sans-serif;color:#3aa7a3;padding-top:10px;border-bottom:1px solid #e5e5e5;padding-bottom:8px}
.popular__list{list-style:none;padding:10px 6px 0 6px;font-size:16px;line-height:26px;color:#555}
.popular__list li{margin-bottom:10px;text-indent:0}
.popular__list li::before{content:"›";color:var(--white);font-weight:700;margin-right:14px}

.footer{position:absolute;left:0;top:3074px;width:1200px;height:241px;background:var(--footer);color:#eee}
.footer__brand{position:absolute;left:150px;top:40px;display:flex;align-items:center;gap:8px;color:var(--white)}
.footer__brand .brand__dot{width:30px;height:30px}
.footer__brand .brand__name{font-size:19px}
.footer__legal{position:absolute;left:153px;top:98px;font-size:11.5px;line-height:17px;width:180px}
.footer__col{position:absolute;top:46px;font-size:11.5px;line-height:17px}
.footer__col h4{font:700 13px 'Lato',sans-serif;color:var(--white);margin-bottom:8px;letter-spacing:.5px}
</style>
</head>
<body>

<div class="topbar">
  <p class="topbar__note">First time visitor? Then start here and learn more about Southern Cross Wealth School!</p>
  <div class="topbar__search">Search
    <svg width="14" height="14" viewBox="0 0 14 14"><circle cx="6" cy="6" r="4.5" fill="none" stroke="#fff" stroke-width="2"/><line x1="9.3" y1="9.3" x2="13" y2="13" stroke="#fff" stroke-width="2"/></svg>
  </div>
</div>

<header class="header">
  <a class="brand" href="#"><span class="brand__dot"></span><span class="brand__name">SOUTHERN CROSS</span></a>
  <div class="header__account"><a href="#">Sign in | Join</a><a href="#">Contact us</a></div>
  <nav class="nav">
    <a href="#">HOME</a><a class="is-active" href="#">BLOG</a><a href="#">PRODUCTS</a><a href="#">ABOUT US</a><a href="#">MEMBERS</a>
  </nav>
</header>

<section class="hero" role="img" aria-label="Teal-tinted photo of a desk with a tablet and an open book">
  <h1 class="hero__title">BLOG</h1>
</section>

<div class="side-tabs"><span></span><span></span><span></span><span></span></div>

<p class="crumbs">Home › <b>Blog</b></p>

<article class="post" style="top:341px">
  <h2 class="post__title">Headline aboun the Title</h2>
  <div class="post__meta"><span>▫ June 10th 2015</span><span>✎ Daniel Harlow</span></div>
  <div class="post__image" role="img" aria-label="Sunny coastal city street with buildings and hills"></div>
  <p class="post__excerpt">Which investment service do you want to receive today?<br>And be successful.</p>
  <div class="share">
    <span class="share__btn share__btn--a"><i></i>1.5k</span>
    <span class="share__btn share__btn--b"><i></i>1.7k</span>
    <span class="share__btn share__btn--off"><i></i>1.1k</span>
    <span class="share__btn share__btn--comments"><i></i>50</span>
  </div>
  <a class="btn-more" href="#">READ MORE</a>
</article>

<article class="post" style="top:1008px">
  <h2 class="post__title">Headline aboun the Title</h2>
  <div class="post__meta"><span>▫ June 10th 2015</span><span>✎ Daniel Harlow</span></div>
  <div class="post__image" role="img" aria-label="Sunny coastal city street with buildings and hills"></div>
  <p class="post__excerpt">Which investment service do you want to receive today?<br>And be successful.</p>
  <div class="share">
    <span class="share__btn share__btn--a"><i></i>1.5k</span>
    <span class="share__btn share__btn--b"><i></i>1.7k</span>
    <span class="share__btn share__btn--c"><i></i>1.1k</span>
    <span class="share__btn share__btn--comments"><i></i>50</span>
  </div>
  <a class="btn-more" href="#">READ MORE</a>
</article>

<article class="post" style="top:1675px">
  <h2 class="post__title">Headline aboun the Title</h2>
  <div class="post__meta"><span>▫ June 10th 2015</span><span>✎ Daniel Harlow</span></div>
  <div class="post__image" role="img" aria-label="Sunny coastal city street with buildings and hills"></div>
  <p class="post__excerpt">Which investment service do you want to receive today?<br>And be successful.</p>
  <div class="share">
    <span class="share__btn share__btn--a"><i></i>1.5k</span>
    <span class="share__btn share__btn--b"><i></i>1.7k</span>
    <span class="share__btn share__btn--c"><i></i>1.1k</span>
    <span class="share__btn share__btn--comments"><i></i>50</span>
  </div>
  <a class="btn-more" href="#">READ MORE</a>
</article>

<article class="post" style="top:2342px">
  <h2 class="post__title">Headline aboun the Title</h2>
  <div class="post__meta"><span>▫ June 10th 2015</span><span>✎ Daniel Harlow</span></div>
  <div class="post__image" role="img" aria-label="Sunny coastal city street with buildings and hills"></div>
  <p class="post__excerpt">Which investment service do you want to receive today?<br>And be successful.</p>
  <div class="share">
    <span class="share__btn share__btn--a"><i></i>1.5k</span>
    <span class="share__btn share__btn--b"><i></i>1.7k</span>
    <span class="share__btn share__btn--c"><i></i>1.1k</span>
    <span class="share__btn share__btn--comments"><i></i>50</span>
  </div>
  <a class="btn-more" href="#">READ MORE</a>
</article>

<aside>
  <a class="cta" href="#" style="top:354px">
    <span class="cta__icon"><svg width="22" height="18" viewBox="0 0 22 18"><path d="M1 2h8l2 2 2-2h8v14h-8l-2 1-2-1H1z" fill="#fff"/><line x1="11" y1="4" x2="11" y2="17" stroke="#6bc9c5" stroke-width="1.5"/></svg></span>
    <span class="cta__label">TEACH ME HOW TO TRADE</span>
  </a>
  <a class="cta" href="#" style="top:418px;background:#5cbcb8">
    <span class="cta__icon"><svg width="20" height="18" viewBox="0 0 20 18"><rect x="1" y="12" width="3" height="6" fill="#fff"/><rect x="6" y="8" width="3" height="10" fill="#fff"/><rect x="11" y="4" width="3" height="14" fill="#fff"/><rect x="16" y="0" width="3" height="18" fill="#fff"/></svg></span>
    <span class="cta__label">TELL ME WHAT SHULD I TRADE</span>
  </a>
  <a class="cta" href="#" style="top:484px">
    <span class="cta__icon"><svg width="22" height="18" viewBox="0 0 22 18"><rect x="1" y="5" width="20" height="12" fill="#fff"/><rect x="7" y="1" width="8" height="5" fill="none" stroke="#fff" stroke-width="2"/></svg></span>
    <span class="cta__label">DO ALL THE WORK FOR ME</span>
  </a>

  <section class="popular">
    <h3 class="popular__title">Popular Posts</h3>
    <ul class="popular__list">
      <li>Buy, then hold and then hope. Not in the current market...</li>
      <li>Farmer's wife trades just like the boys on wall street</li>
    </ul>
  </section>
</aside>

<footer class="footer">
  <div class="footer__brand"><span class="brand__dot"></span><span class="brand__name">SOUTHERN CROSS</span></div>
  <p class="footer__legal">© Copyright 2015 SCWS — All right reserved<br>Terms &amp; Conditions<br>Privacy Policy<br>Contact Us<br>PO BOX Seabrook QLD Coast</p>
  <div class="footer__col" style="left:380px"><h4>MAIN MENU</h4>Home<br>Courses<br>Blog<br>About Us<br>Contact Us</div>
  <div class="footer__col" style="left:535px"><h4>COURSES</h4>Foundation<br>OME<br>Stock<br>Futures<br>Mindset</div>
  <div class="footer__col" style="left:687px"><h4>OTHER</h4>FSG<br>Disclaimers<br>Other Legal</div>
  <div class="footer__col" style="left:844px"><h4>CONNECT US WITH</h4>Chatterly<br>Chirpline<br>Searchly<br>Clipstream</div>
</footer>

</body>
</html>
```